Maplewood Surgery Brochure Design

Maplewood Surgery (maplewoodsurgery.example)

Is a comprehensive breast care center that focuses on caring for women with breast cancer and other breast pathologies. We need a promotional and marketing brochure, in a tri-fold format, to provide information about our office and describe the services that we offer.

Deliverable

* The brochure should be completed by August 24th
* We will need the necessary files to get the brochure printed (.ai, .indd, etc).

Target Market(s)

Primarily patients of age between 30+ and 70+. The brochure will also be placed in doctor's waiting room

Industry/Entity Type

Marketing

Requirements
Must have
• * Make use of the color scheme as the website (http://maplewoodsurgery.example, http://maplewoodsurgery.example/static/theme-fuchsia.png)
* Incorporate the following graphic elements:
* The company’s logo (provided as an attachment)
* At least one images from the homepage
* Photos of the primary doctor and her staff
* Map to show the office location and phone number
* Enclose a breast cancer self-exam card (http://maplewoodsurgery.example/static/shower-card.jpg)
* A portion of the brochure must be detachable and serve as business cards that can be cut off (see attachment).
Nice to have
• Here is an example of a brochure that we like:

http://designbazaro.example/item/flexible-trifold-brochure/318274?WT.ac=search_item&WT.seg_1=search_item&WT.z_author=mendavik

```html
<!DOCTYPE html>
<html lang="en">
<head>
<meta charset="utf-8">
<title>Maplewood Surgery – Trifold Brochure</title>
<link href="https://fonts.googleapis.com/css2?family=Gelasio:wght@400;700&family=Great+Vibes&display=swap" rel="stylesheet">
<style>
  :root {
    --pink: #f4afcd;
    --pink-soft: #f9d3e3;
    --berry: #a3275f;
    --wine: #6b1a2c;
    --ink: #5a2a35;
    --grey: #999999;
    --white: #ffffff;
  }
  * { box-sizing: border-box; margin: 0; padding: 0; }
  html, body { width: 1080px; height: 1200px; overflow: hidden; background: var(--white); }
  body { position: relative; font-family: "Gelasio", Georgia, serif; color: var(--ink); }

  .masthead { position: absolute; top: 0; left: 0; width: 1080px; height: 139px; background: var(--white); }
  .masthead h2 {
    position: absolute; top: 48px; font-family: "Great Vibes", cursive; font-weight: 400;
    font-size: 50px; color: var(--berry); line-height: 1;
  }
  .title-comprehensive { left: 82px; }
  .title-timely { left: 496px; }
  .title-personal { left: 842px; }

  .rule { position: absolute; left: 0; width: 1080px; }
  .rule-light { top: 139px; height: 3px; background: var(--pink); }
  .rule-dark { top: 142px; height: 8px; background: var(--wine); }

  .panel-pink { position: absolute; top: 150px; left: 0; width: 1080px; height: 612px; background: var(--pink); overflow: hidden; }

  .flower-area {
    position: absolute; left: 0; top: 400px; width: 265px; height: 212px;
    background: radial-gradient(ellipse 55% 55% at 40% 55%, var(--pink-soft) 0%, rgba(249,211,227,0.6) 45%, rgba(244,175,205,0) 100%);
  }

  .column { position: absolute; top: 12px; width: 304px; font-size: 12.9px; line-height: 16.7px; hyphens: auto; -webkit-hyphens: auto; }
  .column p { margin-bottom: 16.7px; }
  .col-left { left: 29px; }
  .col-middle { left: 389px; }
  .col-right { left: 749px; width: 310px; }
  .column strong { color: var(--wine); font-weight: 700; }

  .doctor-photo {
    float: right; width: 126px; height: 158px; margin: 0 9px 4px 8px;
    border: 3px solid var(--white); box-shadow: 0 1px 4px rgba(0,0,0,0.35);
    background: linear-gradient(160deg, #7d8a9a 0%, #2c3440 70%, #1d232c 100%);
  }

  .services { list-style: none; margin-bottom: 16.7px; }
  .services li { position: relative; padding-left: 23px; }
  .services li::before { content: "•"; position: absolute; left: 0; }

  .panel-grey { position: absolute; top: 762px; left: 0; width: 709px; height: 438px; background: var(--grey); }

  .cutout-cards { position: absolute; top: 762px; left: 709px; width: 371px; height: 438px; background: var(--white); }
  .business-card { position: absolute; left: 0; width: 371px; height: 219px; transform: rotate(180deg); padding: 34px 30px 0 30px; font-size: 13px; line-height: 16.7px; }
  .card-top { top: 0; }
  .card-bottom { top: 219px; border-bottom: 1px dotted #777; }
  .business-card h3 { font-size: 14px; font-weight: 700; color: var(--wine); margin-bottom: 16.7px; }
  .business-card p { margin-bottom: 16.7px; }
</style>
</head>
<body>
  <header class="masthead">
    <h2 class="title-comprehensive">Comprehensive</h2>
    <h2 class="title-timely">Timely</h2>
    <h2 class="title-personal">Personal</h2>
  </header>
  <div class="rule rule-light"></div>
  <div class="rule rule-dark"></div>

  <section class="panel-pink">
    <div class="flower-area" role="img" aria-label="Soft pink lotus flower photograph"></div>

    <div class="column col-left">
      <p>We provide a caring, intimate environment where your dignity and health come first.</p>
      <p>Conveniently, we are situated next to Brookfield Hospital, in the Harlow Whitfield Cancer Center. This means that any necessary diagnostic and treatment modalities are at our fingertips.</p>
      <p>We understand the anxiety involved with breast problems.</p>
      <p>We know that when you are told that you need to be evaluated more closely, you want answers as quickly as possible.</p>
      <p>We are here to help you, striving to be as proficient as possible.</p>
      <p>Being dedicated to breast care, we have a wealth of up-to-date knowledge about current breast care concepts.</p>
      <p>Your doctor will listen to your concerns and work with you to make sure you understand your options.</p>
      <p>Our knowledgeable staff will help to alleviate your anxiety with timely appointments, education and compassion.</p>
      <p>We will make sure you have all the facts to make the best decisions about your health care.</p>
    </div>

    <div class="column col-middle">
      <p><strong>Dedicated</strong> to bringing to you the most fresh and knowledgeable breast care, including all diagnostic studies and any surgical techniques necessary.</p>
      <p><strong>Unified team approach</strong> - one that includes communication with your primary doctor, laboratory, radiology and ancillary services in a coordinated effort.</p>
      <p><strong>Appropriate resources</strong> - including support groups, therapy, oncology, radiation oncology, cancer societies and more.</p>
      <p><span class="doctor-photo" role="img" aria-label="Portrait photo of Dr. Elena Varga"></span><strong>Experience:</strong><br>
        Dr. Varga has focused her entire practice on breast surgery, as she feels that this is the field in which she excels.<br>
        Being fellowship-trained in Oncoplastic Breast Surgery, she intensely believes in comprehensive breast care and being with the patient through the entire experience. She is comfortable treating patients of all ages, from birth to the elderly. Being compassionate and caring, she strives to project these qualities into everything that she puts her hands on.</p>
      <p>Dr. Varga is passionate about making sure that her patients get the best care, that they are well-informed, and treated with the dignity and respect that they deserve.</p>
    </div>

    <div class="column col-right">
      <p>Dr. Elena Varga is the first fellowship-trained breast surgeon south of Springfield, Illinois, and is excited to come home and bring her expertise to the women of Southern Illinois.</p>
      <p>She deeply understands that you need to heal physically… emotionally… spiritually.</p>
      <p>This is truly comprehensive breast care.</p>
      <p style="margin-bottom:0">Services include:</p>
      <ul class="services">
        <li>Breast pain and other nonsurgical management of breast problems</li>
        <li>Treatment of diseases of the breast (abscesses, gynecomastia)</li>
        <li>Biopsies (including minimally invasive with ultrasound or stereotactic guidance)</li>
        <li>Cryoablation (freezing) of certain breast conditions</li>
        <li>Breast resections (as needed for benign or malignant disease processes)</li>
        <li>Lymph node resections (including sentinel lymph node excisions)</li>
        <li>Breast reconstruction and balancing of the “other” breast as needed</li>
        <li>Breast reductions (for cancer or for burdensome breasts)</li>
        <li>Mastopexies (breast lifts for cancer or droopy breasts)</li>
      </ul>
      <p>Of course, this is not an exhaustive list. If there is a procedure you are interested in, please call our office on (555) 014-2052 to find out if we offer it.</p>
    </div>
  </section>

  <div class="panel-grey"></div>

  <aside class="cutout-cards">
    <div class="business-card card-top">
      <h3>How to Find Us</h3>
      <p>We are located at the Breast Center inside the Harlow Whitfield Cancer Center on the campus of Brookfield Hospital</p>
      <p>4410 Larkspur Dr,<br>Suite 100 Fairhaven, IL 62000<br>Phone: (555) 014-2052<br>Fax: (555) 014-6683</p>
    </div>
    <div class="business-card card-bottom">
      <h3>How to Find Us</h3>
      <p>We are located at the Breast Center inside the Harlow Whitfield Cancer Center on the campus of Brookfield Hospital</p>
      <p>4410 Larkspur Dr,<br>Suite 100 Fairhaven, IL 62000<br>Phone: (555) 014-2052<br>Fax: (555) 014-6683</p>
    </div>
  </aside>
</body>
</html>
```